We Need a Letterhead + Fax Cover Sheet for Heron Staffing

LETTERHEAD:
- Simple letterhead. Please provide an editable .doc file apart from usual Source Files. Logo Files attached for your use.
- Please place our logo on the upper right corner of the page. You may add some sort of graphic, or light colored background (depends on what looks good).
- Footer should include:
Heron Staffing, LLC
412 Kestrel Ave. Suite 118
Mobile, AL 36619

FAX COVER SHEET:
- Have the logo placed here, should be large, maybe an eight of the page.
- Put:
From:
To:
Phone Number:
Fax Number:

*Still needs some details, will update you because working on the website, etc.

Heron Coastal Workforce Services

```html
<!DOCTYPE html>
<html lang="en">
<head>
<meta charset="utf-8">
<title>Heron Staffing — Letterhead and Fax Cover Sheet</title>
<link href="https://fonts.googleapis.com/css2?family=Questrial&family=Roboto:wght@400;700&display=swap" rel="stylesheet">
<style>
  :root {
    --backdrop: #dcdcdc;
    --paper: #f6f6f6;
    --brand-blue: #0b72b0;
    --brand-green: #8aa83a;
    --ink: #3a3a3a;
    --ink-soft: #555;
    --field: #e8e9ea;
    --white: #ffffff;
  }
  * { box-sizing: border-box; margin: 0; padding: 0; }
  html, body { width: 1200px; height: 877px; overflow: hidden; }
  body { background: var(--backdrop); position: relative; font-family: "Questrial", sans-serif; color: var(--ink); }

  .sheet {
    position: absolute; top: 64px; width: 527px; height: 742px;
    background: linear-gradient(90deg, #f3f3f3, #fafafa);
    box-shadow: 0 2px 10px rgba(0,0,0,0.12);
  }
  .sheet--letter { left: 59px; }
  .sheet--fax { left: 622px; }

  .brand-mark {
    position: absolute; left: 372px; top: 58px; width: 120px;
    display: flex; flex-direction: column; align-items: center; gap: 8px;
  }
  .brand-mark__dot { width: 34px; height: 34px; border-radius: 50%; background: var(--brand-green); }
  .brand-mark__name {
    font-family: "Roboto", sans-serif; font-weight: 700; font-size: 13px; line-height: 1.2;
    color: var(--brand-blue); text-align: center; text-transform: uppercase; letter-spacing: 0.5px;
  }

  .footer-band {
    position: absolute; left: 0; top: 692px; width: 100%; height: 22px;
    background: linear-gradient(90deg, var(--brand-blue) 0 83%, var(--brand-green) 83% 100%);
  }
  .footer-band__address {
    position: absolute; left: 42px; top: 5px; font-family: "Roboto", sans-serif;
    font-size: 10px; color: var(--white); white-space: nowrap;
  }
  .footer-band__seal {
    position: absolute; left: 440px; top: -1px; width: 24px; height: 24px;
    border-radius: 50%; background: var(--white); border: 2px solid var(--brand-blue);
  }

  .letter-greeting { position: absolute; left: 47px; top: 196px; font-size: 13.5px; color: var(--ink); }
  .letter-body { position: absolute; left: 47px; top: 227px; width: 440px; }
  .letter-body p { font-size: 7.6px; line-height: 11.4px; color: var(--ink-soft); margin-bottom: 11.4px; text-align: justify; }
  .letter-closing { position: absolute; left: 47px; top: 471px; font-size: 7.6px; color: var(--ink-soft); }
  .letter-signature {
    position: absolute; left: 42px; top: 500px; width: 96px; height: 38px;
    background: linear-gradient(90deg, rgba(11,114,176,0.18), rgba(11,114,176,0.06)); border-radius: 4px;
  }

  .fax-fields {
    position: absolute; left: 46px; top: 191px; width: 436px;
    display: grid; grid-template-columns: 58px 155px 58px 155px; column-gap: 3px; row-gap: 1.6px;
  }
  .fax-fields__label, .fax-fields__value { height: 21.6px; background: var(--field); }
  .fax-fields__label { font-family: "Roboto", sans-serif; font-size: 8.8px; color: var(--ink); padding: 7px 0 0 9px; }

  .fax-flags { position: absolute; left: 48px; top: 292px; width: 420px; }
  .fax-flag { position: absolute; display: flex; align-items: center; gap: 5px; font-family: "Roboto", sans-serif; font-size: 6.6px; color: var(--ink); white-space: nowrap; }
  .fax-flag__box { width: 9px; height: 9px; border: 1px solid #444; background: var(--white); }
  .fax-comments { position: absolute; left: 50px; top: 315px; font-family: "Roboto", sans-serif; font-size: 9.6px; color: var(--ink); }
</style>
</head>
<body>

<section class="sheet sheet--letter" aria-label="Letterhead">
  <div class="brand-mark">
    <span class="brand-mark__dot"></span>
    <span class="brand-mark__name">Heron Coastal Workforce Services</span>
  </div>

  <p class="letter-greeting">Dear Mr. Dalton,</p>

  <div class="letter-body">
    <p>Lorem ipsum dolor sit amet, consectetur adipiscing elit. Donec orci purus, luctus vitae dignissim eu, iaculis sed purus. Vivamus faucibus, ipsum nec aliquet viverra, leo mauris condimentum ligula, sit amet sagittis enim ligula quis arcu. Nam egestas tortor id nisi porttitor mattis. In tortor ante, ultricies in suscipit a, tempus non massa. Vivamus et auctor mi. Fusce vel massa nulla. Phasellus nec eros mauris, et scelerisque orci.</p>
    <p>Donec malesuada orci vitae nulla accumsan porta a id massa. Quisque accumsan iaculis magna sit amet fringilla. Maecenas consequat, magna eget tincidunt semper, odio nibh rutrum mi, id feugiat ante nisi eu risus. Vestibulum nunc orci, rhoncus a placerat in, ultricies in mi. Cras mattis varius eros, vel fringilla nisi suscipit eget. Quisque scelerisque sagittis nulla at porttitor.</p>
    <p>Sed id augue vitae urna euismod commodo aliquet a quam. Pellentesque arcu velit, cursus et malesuada ut, consequat et diam. Nullam erat sem, rhoncus id ullamcorper vitae, rhoncus et arcu. In ultricies ultricies nulla, ut rutrum nisi iaculis at. Donec eu magna a metus ornare faucibus. Fusce aliquet faucibus ultricies. Morbi semper, est id tincidunt gravida, sem arcu adipiscing lacus, ac bibendum nulla leo eu purus. Quisque nec diam sed risus consectetur a accumsan quis quis nibh. Vestibulum id purus lorem.</p>
    <p>It is a long established fact that a reader will be distracted by the readable content of a page when looking at its layout. The point of using Lorem Ipsum is that it has a more-or-less normal distribution of letters, as opposed to using 'Content here, content here', making it look like readable English. Many desktop publishing packages</p>
  </div>

  <p class="letter-closing">Sincerely,</p>
  <div class="letter-signature" role="img" aria-label="Handwritten signature of Evan Dalton"></div>

  <footer class="footer-band">
    <span class="footer-band__address">Heron Staffing, LLC &nbsp;| 412 Kestrel Ave. Suite 118 &nbsp;| Mobile, AL 36619</span>
    <span class="footer-band__seal"></span>
  </footer>
</section>

<section class="sheet sheet--fax" aria-label="Fax cover sheet">
  <div class="brand-mark">
    <span class="brand-mark__dot"></span>
    <span class="brand-mark__name">Heron Coastal Workforce Services</span>
  </div>

  <div class="fax-fields">
    <div class="fax-fields__label">To</div><div class="fax-fields__value"></div>
    <div class="fax-fields__label">From</div><div class="fax-fields__value"></div>
    <div class="fax-fields__label">Fax</div><div class="fax-fields__value"></div>
    <div class="fax-fields__label">Pages</div><div class="fax-fields__value"></div>
    <div class="fax-fields__label">Phone</div><div class="fax-fields__value"></div>
    <div class="fax-fields__label">Date</div><div class="fax-fields__value"></div>
    <div class="fax-fields__label">Re</div><div class="fax-fields__value"></div>
    <div class="fax-fields__label">CC</div><div class="fax-fields__value"></div>
  </div>

  <div class="fax-flags">
    <span class="fax-flag" style="left:0"><span class="fax-flag__box"></span>Urgent</span>
    <span class="fax-flag" style="left:67px"><span class="fax-flag__box"></span>For Review</span>
    <span class="fax-flag" style="left:147px"><span class="fax-flag__box"></span>Please comment</span>
    <span class="fax-flag" style="left:255px;top:1px"><span class="fax-flag__box"></span>Please reply</span>
    <span class="fax-flag" style="left:352px"><span class="fax-flag__box"></span>Please recycle</span>
  </div>

  <p class="fax-comments">Comments :</p>

  <footer class="footer-band">
    <span class="footer-band__address">Heron Staffing, LLC &nbsp;| 412 Kestrel Ave. Suite 118 &nbsp;| Mobile, AL 36619</span>
    <span class="footer-band__seal"></span>
  </footer>
</section>

</body>
</html>
```